Lend a Lantern Website Design (design layout only)

We need a website design for a new nonprofit organization based in Harlow Springs, Iowa called Lend a Lantern. The nonprofit provides soccer training opportunities to youth soccer players looking to improve their game while also affecting the lives of the less fortunate in a positive way. While participating in the training programs the players also go out and raise money for selected charities. The organization then donates the funds. In its first 18 months we donated $10,500. We would like to see designs attempt to symbolize the mission of the nonprofit - essentially "improve you while improving someone else."

We would like to see the following features:

· A place to donate - Our intent is to have the home page linked to the donation page; a simple straight-forward process for people to give money, and make donating as painless as possible - no account needed to make a donation, credit card or e-check should be the only information needed to donate, and have it be on a single page.

· A photo gallery so people can browse the photo gallery to get a better understanding of our organization and a place to add videos and a calendar to show upcoming events

· A place for contact information and the profiles of directors and board members. This should include a spot showing all the charities the organization donates to. Also includes a news section/blog for comments and suggestions.

We want the design to revolve around the content and mission. We would really like to stress our organization as nonprofit. We would also like if the website was user friendly and easy to navigate.

The logo of our organization is uploaded

```html
<!DOCTYPE html>
<html lang="en">
<head>
<meta charset="utf-8">
<title>Lend a Lantern — Home</title>
<link href="https://fonts.googleapis.com/css2?family=Oswald:wght@300;400;500&family=Pathway+Gothic+One&display=swap" rel="stylesheet">
<style>
:root{
  --green-dark:#4a6b2e;
  --green-mid:#5d7f35;
  --green-light:#7fa24f;
  --grey-box:#707073;
  --grey-text:#6b6b6b;
  --grey-btn:#9a9a9a;
  --white:#ffffff;
  --page:#ffffff;
}
*{box-sizing:border-box;margin:0;padding:0}
html,body{width:960px;height:1200px;overflow:hidden;background:var(--page)}
body{position:relative;font-family:"Pathway Gothic One",sans-serif;color:var(--grey-text)}
a{color:inherit}
.abs{position:absolute}

/* header */
.site-header{left:0;top:0;width:960px;height:66px;background:linear-gradient(#fff,#eeeeee);border-bottom:1px solid #d5d5d5}
.brand{left:180px;top:12px;display:flex;align-items:center;gap:8px;font-family:"Oswald",sans-serif;font-weight:500;font-size:27px;color:var(--green-mid);letter-spacing:.5px;text-transform:uppercase}
.brand-mark{width:26px;height:26px;background:var(--green-mid)}
.social{left:636px;top:12px;display:flex;gap:6px}
.social span{width:14px;height:14px;background:var(--grey-btn);border-radius:2px}
.search{left:695px;top:8px;width:85px;height:20px;border:1px solid #c4c4c4;background:#fff;font-size:12px;color:#aaa;padding:2px 0 0 20px}
.search svg{position:absolute;left:4px;top:3px}
.main-nav{right:180px;top:36px;display:flex;gap:13px;font-size:14px;color:var(--green-dark)}

/* hero */
.hero{left:0;top:66px;width:960px;height:302px;background:linear-gradient(160deg,#3f6b2a 0%,#5c8a37 35%,#4c7a2e 60%,#2f5720 100%)}
.hero-title{left:0;top:88px;width:960px;text-align:center;font-family:"Oswald",sans-serif;font-weight:400;font-size:32px;color:#fff;letter-spacing:-.5px;text-shadow:0 1px 3px rgba(0,0,0,.6)}
.hero-text{left:185px;top:140px;width:590px;text-align:center;font-size:16.5px;line-height:17px;color:#fff;text-shadow:0 1px 3px rgba(0,0,0,.8)}
.donate-btn{left:391px;top:232px;width:178px;height:48px;background:var(--green-dark);border:2px solid #fff;color:#fff;font-family:"Oswald",sans-serif;font-size:24px;text-align:center;line-height:43px;letter-spacing:-.5px}
.band{left:0;top:368px;width:960px;height:110px;background:linear-gradient(#d9d9d9,#fff)}

/* feature boxes */
.feature{top:315px;width:200px;height:210px;color:#fff;text-align:center;border:1px solid #cfcfcf}
.feature.events{left:180px;background:var(--green-dark)}
.feature.board{left:380px;background:var(--green-light)}
.feature.charities{left:580px;background:var(--grey-box)}
.feature svg{display:block;margin:11px auto 0}
.feature h2{margin-top:15px;font-family:"Pathway Gothic One",sans-serif;font-weight:400;font-size:19.5px;letter-spacing:0}
.feature ul{list-style:none;margin-top:11px;font-size:12px;line-height:13px}
.feature li{text-decoration:underline}
.feature .more{display:inline-block;margin-top:19px;padding:0 9px;height:25px;line-height:23px;background:var(--grey-btn);border:1px solid #e2e2e2;font-size:12.5px}

/* section headings */
.section-title{display:flex;align-items:center;gap:8px;font-family:"Oswald",sans-serif;font-weight:400;font-size:24px;letter-spacing:-.8px;color:var(--green-dark);text-transform:uppercase}
.section-title .light{color:var(--grey-text);font-weight:300}
.section-title .mark{width:22px;height:22px;background:var(--green-light)}

/* news */
.news-item{left:180px;width:375px;height:68px}
.news-thumb{position:absolute;left:0;top:0;width:67px;height:67px;border:1px solid #bbb;background:linear-gradient(#8fa66a,#4e7a2f)}
.news-body{position:absolute;left:80px;top:0;width:295px}
.news-body h3{font-family:"Pathway Gothic One",sans-serif;font-weight:400;font-size:16px;color:var(--green-dark);text-decoration:underline}
.news-body p{margin-top:10px;font-size:12px;line-height:13px}
.news-body p a{color:var(--green-dark);text-decoration:underline}

/* right column */
.video{left:581px;top:600px;width:199px;height:119px;background:linear-gradient(#5d7d3e 0%,#6f8f4a 40%,#5a7a3a 100%);border:1px solid #444}
.small-link{font-size:12px;text-decoration:underline}
.photo{width:62px;height:45px;border:1px solid #999;background:linear-gradient(#3c6a2c,#6f9a45)}

/* footer */
.site-footer{left:0;top:988px;width:960px;height:212px;background:var(--green-dark);border-top:2px solid #aaa}
.footer-col{color:#fff}
.footer-col h4{font-family:"Oswald",sans-serif;font-weight:400;font-size:16px;letter-spacing:-.3px;color:#fff}
.footer-col p{margin-top:12px;font-size:11.5px;line-height:12px}
.quick-links{list-style:none;margin-top:13px;font-size:11.5px;line-height:11.6px}
.quick-links li{text-decoration:underline}
.email-field{margin-top:13px;width:118px;height:19px;background:#fff;border:1px solid #ccc}
.subscribe-btn{margin-top:10px;width:72px;height:20px;background:var(--grey-btn);border:1px solid #ddd;font-size:12px;text-align:center;line-height:18px}
.map{left:580px;top:1071px;width:199px;height:115px;background:linear-gradient(135deg,#eef0e6,#dfe5d6);border:1px solid #bbb}
</style>
</head>
<body>

<header class="site-header abs"></header>
<div class="brand abs"><span class="brand-mark"></span>Lend a Lantern</div>
<div class="social abs" aria-label="Social links"><span></span><span></span><span></span></div>
<div class="search abs">
  <svg width="11" height="11" viewBox="0 0 11 11"><circle cx="4.5" cy="4.5" r="3.5" fill="none" stroke="#999" stroke-width="1.4"/><line x1="7" y1="7" x2="10" y2="10" stroke="#999" stroke-width="1.4"/></svg>
  Search
</div>
<nav class="main-nav abs">
  <span>Donate</span><span>News</span><span>Photos &amp; Videos</span><span>Events</span><span>Board Members</span><span>Charities</span><span>Contact</span>
</nav>

<section class="hero abs" role="img" aria-label="Photo of youth soccer players on a grass field chasing a ball"></section>
<h1 class="hero-title abs">WELCOME TO LEND A LANTERN</h1>
<p class="hero-text abs">Based in Harlow Springs, IA, our nonprofit organization provides soccer training opportunities to youth soccer players looking to improve their game while also affecting the lives of the less fortunate in a positive way. While participating in the training programs, players also go out and raise money for selected charities to which Lend a Lantern then donates the funds. In our first 18 months, we donated over $10,500 to charities.</p>
<div class="donate-btn abs">DONATE NOW!</div>
<div class="band abs"></div>

<section class="feature events abs">
  <svg width="38" height="38" viewBox="0 0 38 38"><circle cx="19" cy="19" r="16" fill="none" stroke="#fff" stroke-width="3"/><polygon points="19,13 25,17.5 23,24 15,24 13,17.5" fill="#fff"/></svg>
  <h2>UPCOMING EVENTS</h2>
  <ul>
    <li>9/6/14 at 12 PM: Game against XXXXXX</li>
    <li>9/13/14 at 12 PM: Game against XXXXXX</li>
    <li>9/20/14 at 12 PM: Game against XXXXXX</li>
    <li>9/27/14 at 12 PM: Game against XXXXXX</li>
  </ul>
  <span class="more">More Events...</span>
</section>
<section class="feature board abs">
  <svg width="38" height="38" viewBox="0 0 38 38"><circle cx="24" cy="8" r="6" fill="#fff"/><path d="M15 23c0-5 4-8 9-8s9 3 9 8z" fill="#fff"/><circle cx="12" cy="20" r="5" fill="#fff"/><path d="M4 35c0-5 3-8 8-8s8 3 8 8z" fill="#fff"/></svg>
  <h2>MEET OUR BOARD MEMBERS</h2>
  <ul><li>Ann Weller</li><li>Mia Corbett</li><li>Ray Dalton</li><li>Lena Hart</li></ul>
  <span class="more">All Bios...</span>
</section>
<section class="feature charities abs">
  <svg width="38" height="38" viewBox="0 0 38 38"><polygon points="19,3 36,19 31,19 31,35 23,35 23,25 15,25 15,35 7,35 7,19 2,19" fill="#fff"/></svg>
  <h2>CHARITIES WE SUPPORT</h2>
  <ul><li>Harbor Relief Fund</li><li>Bright Wish Network</li><li>Second Chance Shop</li><li>Open Door Mission</li></ul>
  <span class="more">More Charities...</span>
</section>

<h2 class="section-title abs" style="left:180px;top:558px"><span class="mark"></span>News <span class="light">&amp; Announcements</span></h2>

<article class="news-item abs" style="top:600px">
  <div class="news-thumb" role="img" aria-label="Soccer ball resting in grass"></div>
  <div class="news-body"><h3>News Item Title Goes Here</h3><p>Lorem ipsum dolor sit amet, consectetur adipiscing elit. Praesent suscipit, mauris eget facilisis commodo, est metus rhoncus diam, at iaculis justo mauris at augue. Vestibulum fringilla mauris sed ornare feugiat. <a>Read more...</a></p></div>
</article>
<article class="news-item abs" style="top:691px">
  <div class="news-thumb" role="img" aria-label="Young players running after the ball"></div>
  <div class="news-body"><h3>News Item Title Goes Here</h3><p>Lorem ipsum dolor sit amet, consectetur adipiscing elit. Praesent suscipit, mauris eget facilisis commodo, est metus rhoncus diam, at iaculis justo mauris at augue. Vestibulum fringilla mauris sed ornare feugiat. <a>Read more...</a></p></div>
</article>
<article class="news-item abs" style="top:785px">
  <div class="news-thumb" role="img" aria-label="Goalkeeper reaching up in front of the net" style="background:linear-gradient(#d8d8d8,#8a8a8a)"></div>
  <div class="news-body"><h3>News Item Title Goes Here</h3><p>Lorem ipsum dolor sit amet, consectetur adipiscing elit. Praesent suscipit, mauris eget facilisis commodo, est metus rhoncus diam, at iaculis justo mauris at augue. Vestibulum fringilla mauris sed ornare feugiat. <a>Read more...</a></p></div>
</article>
<article class="news-item abs" style="top:876px">
  <div class="news-thumb" role="img" aria-label="Two players contesting the ball"></div>
  <div class="news-body"><h3>News Item Title Goes Here</h3><p>Lorem ipsum dolor sit amet, consectetur adipiscing elit. Praesent suscipit, mauris eget facilisis commodo, est metus rhoncus diam, at iaculis justo mauris at augue. Vestibulum fringilla mauris sed ornare feugiat. <a>Read more...</a></p></div>
</article>

<h2 class="section-title abs" style="left:580px;top:558px"><span class="mark"></span>Featured <span class="light">Video</span></h2>
<div class="video abs" role="img" aria-label="Video still of a youth soccer match on a field"></div>
<span class="small-link abs" style="left:582px;top:726px">View More Videos...</span>

<h2 class="section-title abs" style="left:580px;top:758px"><span class="mark"></span>Recent <span class="light">Photos</span></h2>
<div class="photo abs" style="left:581px;top:801px" role="img" aria-label="Match photo"></div>
<div class="photo abs" style="left:650px;top:801px" role="img" aria-label="Match photo"></div>
<div class="photo abs" style="left:718px;top:801px" role="img" aria-label="Match photo"></div>
<div class="photo abs" style="left:581px;top:851px" role="img" aria-label="Match photo"></div>
<div class="photo abs" style="left:650px;top:851px" role="img" aria-label="Match photo"></div>
<div class="photo abs" style="left:718px;top:851px" role="img" aria-label="Match photo"></div>
<span class="small-link abs" style="left:582px;top:907px">View More Photos...</span>

<footer class="site-footer abs"></footer>
<div class="footer-col abs" style="left:180px;top:1004px">
  <h4>QUICK LINKS</h4>
  <ul class="quick-links"><li>Donate</li><li>News</li><li>Photos &amp; Videos</li><li>Events</li><li>Board Members</li><li>Charities</li><li>Contact</li></ul>
</div>
<div class="footer-col abs" style="left:380px;top:1004px;width:180px">
  <h4>SUBSCRIBE</h4>
  <p>Subscribe to our newsletter by entering your email address in the box below.</p>
  <div class="email-field"></div>
  <div class="subscribe-btn">Subscribe</div>
</div>
<div class="footer-col abs" style="left:580px;top:1004px;width:200px">
  <h4>MAP &amp; DIRECTIONS</h4>
  <p>Our home field is located at 456 Elm Street, Harlow Springs, IA. Click on the map below for directions.</p>
</div>
<div class="map abs" role="img" aria-label="Street map showing the location of the home field"></div>

</body>
</html>
```